New Design for our Velorin Gran Reserva Brandy, it is the label design for the bottle label

We need a new bottle label for our Brandy Gran Reserva that we want to bring to the market.

Please have a look at all our current bottles and labels and the feel of our company under www.velorin-example.ch

The bottle that we will be using for the brand is a different one than the one that we already have, the design of the bottle is attached with a document.

I have also attached a briefing in regards to Brandy in general for your information.

### 1. What is Brandy?
Brandy is a distilled spirit made from fermented wine or other fruit wines. It is traditionally aged in oak barrels, which gives it its characteristic color and rich flavor. The aging process in oak is essential for developing the aromas and quality of the brandy.

### 2. What is Brandy Reserva?
A Brandy labeled as "Reserva" has undergone a longer aging process, typically at least 2 to 3 years, in oak barrels. This aging gives the brandy a deeper, more complex flavor profile and a darker color. "Reserva" is often an indication of higher quality.

### 3. Who enjoys drinking Brandy?
Brandy is typically favored by those who appreciate a deep, rich tasting experience. This often includes older consumers who value the time-aged complexity of the spirit. However, Brandy is also gaining popularity among younger people, especially through cocktails and modern serving styles.

### 4. Why is Brandy trending?
Brandy is experiencing a resurgence as consumers increasingly value quality and artisanal production methods. Its versatility in cocktails and association with traditional, luxurious experiences have also contributed to its renewed popularity.

### 5. What colors would be associated with Brandy?
The typical colors associated with Brandy are warm gold, amber, and deep golden-brown tones. These colors reflect the aging process in oak barrels and the richness of the flavors. Other associated colors might include dark brown and mahogany.

### 6. What is important to customers when buying Brandy?
Customers care about the origin of the Brandy, the aging time, the quality of the ingredients, the production method, and the brand. They also pay attention to the prestige of the product and the authenticity of the production.

### 7. What is not important to customers when buying Brandy?
For many customers, the price and packaging (unless it’s especially exclusive) may be less important than the quality and taste of the Brandy. The distillery name might be less significant if it isn’t tied to a particular reputation.

### 8. What do customers know about Swiss Brandy?
Swiss Brandy is still relatively unknown in many markets, but customers who are familiar with it appreciate the precision and quality of Swiss production. Swiss Brandy is assumed to be made with care and under strict quality standards.

### 9. What is Brandy Gran Reserva?
**Brandy Gran Reserva** is an even higher quality and longer-aged version of Brandy. Generally, a Gran Reserva is aged for at least 5 to 10 years or more in oak barrels. This extended aging process gives the Brandy an especially deep, complex flavor profile and often a darker, richer color. Gran Reserva is often regarded as the top-tier product within a Brandy range and appeals to discerning consumers who value quality, refinement, and a luxurious tasting experience.

The label “Gran Reserva” thus indicates the highest quality level for Brandies, similar to other spirits (like wine or whisky), where the aging time is a critical factor.

### 10. What emotions are associated with Brandy?
Brandy is often associated with luxury, relaxation, and comfort. It evokes feelings of tradition, elegance, and sophistication. Drinking Brandy is frequently seen as a moment of reflection and enjoyment.

### 11. How should Brandy be marketed?
Brandy should be marketed with a focus on its artisanal production, quality, and tradition. A narrative around the product, its aging, and origin can help create an emotional connection with the customer. The marketing should also emphasize the versatility of Brandy, whether consumed neat or in cocktails.

### 12. Sales test and label design for Velorin Brandy
For a sales test, I would suggest a tasting in an upscale setting, perhaps paired with a storytelling presentation highlighting the history of the 6-year aged Brandy and its aging in oak barrels.

**Label design**:
The label should reflect the exclusivity of the product, with an elegant, minimalist design. Colors like deep gold, mahogany, and a hint of deep blue could be used to emphasize the aging and quality of the Brandy. The label should include information about the aging time, the use of oak barrels, and a brief story about the Brandy’s production. A seal or embossing highlighting the craftsmanship would also be fitting.

Target Market(s)

Customers that like Brandy

Requirements
Must have
• the Alcohol % must be included on the label as well as our address.

```html
<!DOCTYPE html>
<html lang="en">
<head>
<meta charset="utf-8">
<title>Velorin Gran Reserva Brandy – Bottle Label</title>
<link rel="stylesheet" href="https://fonts.googleapis.com/css2?family=Bebas+Neue&family=Dancing+Script:wght@600&display=swap">
<style>
  :root {
    --label-black: #000000;
    --gold: #c9a42a;
    --gold-light: #d6b84e;
    --gold-deep: #6e5912;
    --paper: #f4f4f4;
    --white: #ffffff;
    --swiss-red: #e3212b;
  }
  * { margin: 0; padding: 0; box-sizing: border-box; }
  html, body { width: 960px; height: 1200px; overflow: hidden; background: var(--label-black); }
  .label {
    position: relative;
    width: 960px;
    height: 1200px;
    background: var(--label-black);
    overflow: hidden;
    font-family: "Bebas Neue", "Arial Narrow", sans-serif;
  }
  .brand-name {
    position: absolute;
    top: 58px;
    left: 700px;
    width: 200px;
    text-align: center;
    color: var(--gold);
    line-height: 1;
  }
  .brand-name .brand-word { display: block; font-size: 62px; letter-spacing: 2px; }
  .brand-name .brand-descriptor { display: block; font-size: 25px; line-height: 24px; letter-spacing: 2px; margin-top: 2px; }
  .orchard-artwork, .hex-emblem {
    position: absolute;
    left: 0;
    top: 0;
  }
  .swiss-flag {
    position: absolute;
    left: 472px;
    top: 334px;
  }
  .spirit-type {
    position: absolute;
    left: 395px;
    top: 376px;
    width: 200px;
    text-align: center;
    font-family: "Dancing Script", cursive;
    font-weight: 600;
    font-size: 44px;
    color: var(--gold);
    line-height: 1;
    transform: rotate(-4deg);
  }
  .product-title {
    position: absolute;
    left: 295px;
    top: 436px;
    width: 400px;
    text-align: center;
    color: var(--label-black);
    font-weight: 400;
    font-size: 114px;
    line-height: 95px;
    letter-spacing: 1px;
  }
  .age-seal {
    position: absolute;
    left: 447px;
    top: 627px;
  }
  .producer-address {
    position: absolute;
    left: 217px;
    top: 864px;
    color: var(--gold);
    font-style: normal;
    font-size: 15px;
    line-height: 17px;
    letter-spacing: 0.2px;
  }
  .alcohol-volume {
    position: absolute;
    left: 640px;
    top: 904px;
    color: var(--gold);
    font-size: 27px;
    line-height: 1;
  }
  .alcohol-volume .unit { font-size: 18px; }
  .story-band {
    position: absolute;
    left: 0;
    top: 992px;
    width: 960px;
    height: 152px;
    border-top: 3px solid var(--white);
    border-bottom: 4px solid var(--white);
    padding: 3px 0;
    background: var(--label-black);
  }
  .story-panel {
    position: relative;
    width: 100%;
    height: 100%;
    background: var(--paper);
  }
  .barrel-artwork {
    position: absolute;
    left: 16px;
    top: 2px;
    width: 120px;
    height: 134px;
    background: linear-gradient(90deg, #d6d6d6, #efefef 50%, #d0d0d0);
  }
  .brandy-story {
    position: absolute;
    left: 157px;
    top: 19px;
    width: 745px;
    color: var(--gold);
    font-size: 17.4px;
    line-height: 20.5px;
  }
</style>
</head>
<body>
<main class="label">

  <svg class="orchard-artwork" width="960" height="1200" viewBox="0 0 960 1200" role="img" aria-label="Engraved golden apple with leafy branch illustration behind the emblem">
    <defs>
      <radialGradient id="orchard-gold" cx="50%" cy="52%" r="62%">
        <stop offset="0%" stop-color="var(--gold-light)"/>
        <stop offset="60%" stop-color="var(--gold)"/>
        <stop offset="100%" stop-color="var(--gold-deep)"/>
      </radialGradient>
    </defs>
    <rect x="114" y="129" width="766" height="820" rx="24" fill="url(#orchard-gold)"/>
  </svg>

  <div class="brand-name">
    <span class="brand-word">Velorin</span>
    <span class="brand-descriptor">Swiss Distillery</span>
  </div>

  <svg class="hex-emblem" width="960" height="1200" viewBox="0 0 960 1200" aria-hidden="true">
    <defs>
      <polygon id="hex-shape" points="0,-241 211,-120 211,120 0,241 -211,120 -211,-120"/>
    </defs>
    <g transform="translate(495 524)">
      <use href="#hex-shape" fill="var(--white)"/>
      <use href="#hex-shape" fill="var(--label-black)" transform="scale(0.985)"/>
      <use href="#hex-shape" fill="var(--white)" transform="scale(0.955)"/>
      <use href="#hex-shape" fill="var(--label-black)" transform="scale(0.946)"/>
      <use href="#hex-shape" fill="var(--paper)" transform="scale(0.925)"/>
    </g>
  </svg>

  <svg class="swiss-flag" width="46" height="32" viewBox="0 0 46 32" role="img" aria-label="Swiss flag">
    <rect width="46" height="32" fill="var(--swiss-red)"/>
    <rect x="20" y="7" width="6" height="18" fill="var(--white)"/>
    <rect x="14" y="13" width="18" height="6" fill="var(--white)"/>
  </svg>

  <div class="spirit-type">brandy</div>

  <h1 class="product-title">Gran<br>Reserva</h1>

  <svg class="age-seal" width="96" height="96" viewBox="0 0 96 96" role="img" aria-label="Aged for 10 years in oak barrels">
    <defs>
      <path id="seal-top-arc" d="M22 44 A26 26 0 0 1 74 44"/>
      <path id="seal-bottom-arc" d="M16 56 A33 33 0 0 0 80 56"/>
    </defs>
    <circle cx="48" cy="48" r="46" fill="var(--label-black)"/>
    <circle cx="48" cy="48" r="43" fill="none" stroke="var(--gold)" stroke-width="1.2"/>
    <text font-family="Dancing Script, cursive" font-size="9" fill="var(--white)" text-anchor="middle">
      <textPath href="#seal-top-arc" startOffset="50%">aged for</textPath>
    </text>
    <text font-family="Dancing Script, cursive" font-size="8.5" fill="var(--white)" text-anchor="middle">
      <textPath href="#seal-bottom-arc" startOffset="50%">years in oak barrels</textPath>
    </text>
    <text x="48" y="64" font-family="Bebas Neue, sans-serif" font-size="44" fill="var(--gold)" text-anchor="middle">10</text>
    <path d="M13 48 l2 -1 l1 -4 l1 4 l2 1 l-2 1 l-1 4 l-1 -4 z" fill="var(--white)"/>
    <path d="M77 48 l2 -1 l1 -4 l1 4 l2 1 l-2 1 l-1 4 l-1 -4 z" fill="var(--white)"/>
  </svg>

  <address class="producer-address">
    Velorin Swiss Distillery GmbH<br>
    Talackerweg 14<br>
    CH-9999 Obertal - Rebhalde<br>
    +41 00 555 01 23<br>
    info@velorin-example.ch
  </address>

  <div class="alcohol-volume">35-60% <span class="unit">VOL</span></div>

  <section class="story-band">
    <div class="story-panel">
      <div class="barrel-artwork" role="img" aria-label="Engraved oak barrel illustration"></div>
      <p class="brandy-story">
        Brandy Gran Reserva is an even higher quality and longer-aged version of brandy. Generally, a Gran Reserva is aged for 10 years or more in oak barrels. This extended aging process gives the brandy an especially deep, complex flavor profile and often a darker, richer color. Gran Reserva is often regarded as the top-tier product within a brandy range and appeals to discerning consumers who value quality, refinement, and a luxurious tasting experience.
      </p>
    </div>
  </section>

</main>
</body>
</html>
```